Career Drop Down Layout on CopperTrailhead.com Quiz Results

We want to redesign the career drop down view after people take the career finder quiz at CopperTrailhead.com. After you take the quiz (feel free to take it yourself), you get a results page. On the left hand navigation bar, go to Career Matches (in green). When you open one of your career matches, we want people to see lots of great information about the job. We need help figuring out how to display the information. The information we want to display is the following:

1) name of job
2) JOBLEX description
3) Link to the Joblex info
4) Match dial
5) Rising Demand image
6) a video about the job
7) Average salary
8) Minimum Qualifications
9) Top Tips
10) Recommended Programs
11) Jobs in their area - by Hire Lantern

I put screen shots of what we have now and a mock-up of the new elements in the brief. It can look anyway you think will be good. I'm not tied to the mock-up at all.

To see how your design will look live on the web do the following:

1) Login at: https://www.coppertrailhead.com/survey/login (or take the quiz yourself to see your own results)
2) Enter Email address: dana.kowal@copperventure.org
3) Enter Password: 123456
4) See results summary - Click on Career Matches from the left navigation bar
5) See the career matches, when you click the arrow on the right side of each career match it will display the new page you are designing for each career with info from a database.

Thanks, Dana

Target Market(s)

Young people looking for jobs

Number of Pages Required

1 page

Requirements
Must have
• The layout of how all the information will look nicely on a computer screen. It can scroll down more vertically if necessary.

The color scheme and text must match the existing site since this page will be embedded in our site. I attached our design guide.
Nice to have
• I'd like to see a very easy to scan, organized way to display a lot of job information.

```html
<!DOCTYPE html>
<html lang="en">
<head>
<meta charset="utf-8">
<title>Career Matches – Copper Trailhead</title>
<link href="https://fonts.googleapis.com/css2?family=Quicksand:wght@500;600;700&family=Montserrat:ital,wght@0,400;0,500;0,600;0,700;1,400&family=Lato:wght@400;700;900&display=swap" rel="stylesheet">
<style>
:root{
  --indigo:#4f3f99;
  --indigo-deep:#3b2e7e;
  --lavender:#e4e0fa;
  --lavender-bar:#e3e0f6;
  --soft-purple:#9a8fd0;
  --green:#6cc04a;
  --green-active:#3f7a45;
  --pale-green:#e5f1dc;
  --panel:#f5f5f5;
  --ink:#222;
  --muted:#8a84b8;
  --orange:#f39a1e;
  --red:#e0282e;
  --dark:#1d1b22;
  --line:#e4e4ea;
}
*{box-sizing:border-box;margin:0;padding:0}
html,body{width:1200px;height:2601px;overflow:hidden}
body{position:relative;background:#fff;font-family:'Montserrat',sans-serif;color:var(--ink)}
.abs{position:absolute}
.site-header{position:absolute;left:0;top:0;width:1200px;height:75px;background:#fff;border-bottom:1px solid #ddd}
.brand{position:absolute;left:23px;top:28px;display:flex;align-items:center;gap:8px;font-family:'Quicksand',sans-serif;font-weight:700;font-size:20px;color:var(--indigo)}
.brand-dot{width:14px;height:14px;border-radius:50%;background:var(--green)}
.main-nav{position:absolute;top:30px;font-family:'Lato',sans-serif;font-size:12.5px;color:#333;letter-spacing:.2px}
.logout{position:absolute;left:1068px;top:15px;width:94px;height:44px;border-radius:22px;background:var(--indigo);color:#fff;font-family:'Lato',sans-serif;font-weight:900;font-size:12px;display:flex;align-items:center;justify-content:center;letter-spacing:-.3px}
.sidebar{position:absolute;left:0;top:75px;width:267px;height:2337px;background:var(--indigo)}
.sidebar h2{position:absolute;top:40px;width:100%;text-align:center;color:#fff;font-family:'Lato',sans-serif;font-weight:700;font-size:23px;letter-spacing:-.4px}
.side-menu{position:absolute;top:105px;width:100%;list-style:none;border-top:1px solid rgba(255,255,255,.25)}
.side-menu li{height:34.3px;border-bottom:1px solid rgba(255,255,255,.25);color:#fff;font-family:'Lato',sans-serif;font-size:14.5px;text-align:center;line-height:34px}
.side-menu li.active{background:var(--green-active);font-weight:700}
.pdf-btn{position:absolute;left:38px;top:391px;width:176px;height:34px;border-radius:17px;background:var(--green);color:#fff;font-family:'Lato',sans-serif;font-size:16px;text-align:center;line-height:34px;box-shadow:0 2px 3px rgba(0,0,0,.25)}
.hero{position:absolute;left:267px;top:75px;width:933px;height:420px}
.hero-title{position:absolute;left:267px;width:933px;text-align:center;font-family:'Quicksand',sans-serif;font-weight:700;color:#2a2a2a}
.legend{position:absolute;left:452px;top:316px;display:flex;align-items:center;gap:6px;font-size:15px;color:#333}
.legend .gap{width:20px}
.rate-ico{width:30px;height:30px}
.card{position:absolute;left:305px;top:535px;width:857px;height:1830px;background:#fff;border:1px solid var(--line)}
.panel{position:absolute;left:324px;top:592px;width:818px;height:1752px;background:var(--panel);border:1px solid var(--line)}
.career-pill{position:absolute;left:626px;top:511px;width:252px;height:46px;border-radius:23px;background:var(--indigo-deep);color:#fff;font-family:'Quicksand',sans-serif;font-weight:700;font-size:17px;line-height:46px;padding-left:56px}
.bar{position:absolute;left:324px;top:592px;width:818px;height:48px;background:var(--lavender-bar)}
.bar h3{position:absolute;left:18px;top:12px;font-family:'Quicksand',sans-serif;font-weight:700;font-size:18px;letter-spacing:.3px;color:#222}
.side-col{position:absolute;left:895px;top:640px;width:247px;height:922px;background:var(--pale-green)}
.lbl{position:absolute;left:343px;font-family:'Quicksand',sans-serif;font-weight:700;font-size:16.5px;color:#222}
.desc{position:absolute;left:343px;top:711px;width:535px;font-size:14px;line-height:23px;color:#333}
.btn{position:absolute;left:343px;height:48px;border-radius:24px;color:#fff;font-size:11.5px;font-weight:700;letter-spacing:.6px;display:flex;align-items:center;justify-content:center}
.btn.soft{background:var(--soft-purple)}
.btn.deep{background:var(--indigo-deep)}
.tip{position:absolute;left:343px;width:530px;font-size:14px;line-height:23px;color:#333;padding-left:23px}
.tip svg{position:absolute;left:0;top:6px}
.badge{position:absolute;width:77px;height:77px}
.prog-link{position:absolute;font-size:15.5px;line-height:23px;color:var(--indigo);text-decoration:underline}
.center-col{position:absolute;left:895px;width:247px;text-align:center}
.salary{position:absolute;left:943px;top:889px;width:152px;height:48px;border-radius:24px;background:var(--green);color:#fff;font-family:'Quicksand',sans-serif;font-weight:700;font-size:19px;text-align:center;line-height:48px}
.outlook{display:flex;align-items:center;justify-content:center;gap:8px;font-family:'Quicksand',sans-serif;font-weight:700;font-size:22px;color:var(--orange)}
.outlook i{width:14px;height:14px;border-radius:50%;background:var(--orange);display:block}
.video{position:absolute;left:895px;top:1080px;width:247px;height:247px;border-top-right-radius:124px;background:linear-gradient(135deg,#5a4a3c,#2d2a2c 55%,#8a7a6a)}
.jobs-by{position:absolute;left:343px;top:1640px;display:flex;align-items:center;gap:34px}
.jobs-by span{font-family:'Quicksand',sans-serif;font-weight:700;font-size:24px;color:var(--indigo)}
.jobs-by b{display:flex;align-items:center;gap:8px;font-family:'Quicksand',sans-serif;font-weight:700;font-size:24px;color:#222}
.jobs-by i{width:16px;height:16px;background:var(--green);display:block}
.field-lbl{position:absolute;top:1720px;font-size:15px;font-weight:500;color:#222}
.field{position:absolute;height:48px;border:1px solid #e2e2e2;border-radius:24px;background:#fff;font-size:14px;color:#999;line-height:46px;padding-left:26px;width:276px}
.field svg{position:absolute;right:18px;top:19px}
.search{position:absolute;left:933px;top:1751px;width:190px;height:48px;border-radius:24px;background:var(--green);color:#fff;font-size:11.5px;font-weight:700;letter-spacing:.6px;text-align:center;line-height:48px}
.result{position:absolute;left:341px;top:1918px;font-size:18px;color:#6a2a5a}
.result b{color:#6a2a5a;font-weight:700}
.job-title{position:absolute;left:343px;top:1978px;font-family:'Quicksand',sans-serif;font-weight:700;font-size:17px;color:var(--indigo)}
.meta{position:absolute;left:343px;display:flex;align-items:center;gap:6px;font-size:15.5px;color:var(--muted)}
.meta .sp{width:22px}
.job-desc{position:absolute;left:343px;width:760px;font-size:14px;line-height:23px;color:#333}
.footer{position:absolute;left:0;top:2412px;width:1200px;height:151px;background:#f6f6f6}
.social{position:absolute;top:2451px;width:48px;height:48px;border-radius:50%;background:var(--indigo-deep)}
.social.alt{background:var(--green)}
.foot-links{position:absolute;top:2522px;left:0;width:1190px;text-align:center;font-size:17.5px;color:var(--indigo-deep)}
.foot-links span{margin:0 18px}
.copy{position:absolute;left:0;top:2565px;width:1200px;height:36px;background:var(--dark);color:#fff;font-size:14.5px;text-align:center;line-height:36px}
</style>
</head>
<body>

<header class="site-header">
  <div class="brand"><span class="brand-dot"></span>Copper Trailhead</div>
  <nav>
    <span class="main-nav" style="left:796px">HOME</span>
    <span class="main-nav" style="left:862px">MY RESULTS ˅</span>
    <span class="main-nav" style="left:972px">SERVICES ˅</span>
  </nav>
  <div class="logout">LOG OUT</div>
</header>

<aside class="sidebar">
  <h2>Dana's Results</h2>
  <ul class="side-menu">
    <li>Results Summary</li>
    <li>What Motivates You</li>
    <li>Your DISC Profile</li>
    <li class="active">Career Matches</li>
    <li>Maximize My Results</li>
    <li>Communication Tips</li>
    <li>Reflections and Goals</li>
    <li>Resources</li>
  </ul>
  <div class="pdf-btn">Download PDF</div>
</aside>

<svg class="hero" viewBox="0 0 933 420" preserveAspectRatio="none" aria-hidden="true">
  <path d="M0 0H933V340C880 380 820 330 760 350C690 372 640 395 560 385C480 375 430 330 350 345C260 360 200 350 120 360C70 366 30 360 0 395Z" fill="#e2defa"/>
  <path d="M0 395C30 360 70 366 120 360C200 350 260 360 350 345C430 330 480 375 560 385C640 395 690 372 760 350C820 330 880 380 933 340V360C880 395 820 350 760 370C690 392 640 410 560 400C480 392 430 350 350 362C260 378 200 368 120 376C70 382 30 378 0 410Z" fill="#ebe8fb"/>
</svg>

<div class="abs" role="img" aria-label="Career signpost icon" style="left:695px;top:123px;width:76px;height:76px;border-radius:50%;background:var(--green)"></div>
<div class="hero-title" style="top:212px;font-size:28px">Career Matches</div>
<div class="hero-title" style="top:272px;font-size:22px;font-weight:500">Rate as many jobs as you can</div>
<div class="legend">
  <svg class="rate-ico" viewBox="0 0 30 30"><circle cx="15" cy="15" r="13" fill="var(--green)" stroke="#333" stroke-width="1.5"/><path d="M9 17l6-6 6 6" fill="none" stroke="#fff" stroke-width="2.5"/></svg>
  <span>Send to favorites,</span><span class="gap"></span>
  <svg class="rate-ico" viewBox="0 0 30 30"><circle cx="15" cy="15" r="13" fill="#c8c8c8" stroke="#333" stroke-width="1.5"/><path d="M9 15h12" stroke="#333" stroke-width="2.5"/></svg>
  <span>Not sure,</span><span class="gap"></span>
  <svg class="rate-ico" viewBox="0 0 30 30"><circle cx="15" cy="15" r="13" fill="var(--red)" stroke="#333" stroke-width="1.5"/><path d="M9 13l6 6 6-6" fill="none" stroke="#fff" stroke-width="2.5"/></svg>
  <span>No way - send to archive!</span>
</div>
<div class="hero-title" style="top:358px;font-size:14px;font-family:'Montserrat',sans-serif;font-weight:400;font-style:italic;color:#333">Click on each category for in-depth descriptions, resources, education options, and tips.</div>

<section class="card"></section>
<div class="panel"></div>
<div class="career-pill">Holistic Development</div>
<div class="abs" role="img" aria-label="Holistic development person icon" style="left:588px;top:497px;width:76px;height:76px;border-radius:50%;background:var(--green);border:3px solid #fff"></div>

<div class="bar">
  <h3>LIFE COACHING</h3>
  <svg class="abs" style="left:608px;top:11px" width="110" height="28" viewBox="0 0 110 28">
    <circle cx="14" cy="14" r="12" fill="var(--green)" stroke="#333" stroke-width="1.3"/><path d="M9 16l5-5 5 5" fill="none" stroke="#fff" stroke-width="2.2"/>
    <circle cx="52" cy="14" r="12" fill="#c8c8c8" stroke="#333" stroke-width="1.3"/><path d="M47 14h10" stroke="#333" stroke-width="2.2"/>
    <circle cx="90" cy="14" r="12" fill="var(--red)" stroke="#333" stroke-width="1.3"/><path d="M85 12l5 5 5-5" fill="none" stroke="#fff" stroke-width="2.2"/>
  </svg>
  <svg class="abs" style="left:780px;top:15px" width="20" height="20" viewBox="0 0 20 20"><circle cx="10" cy="10" r="8.5" fill="none" stroke="#555" stroke-width="1.3"/><path d="M6 10h8" stroke="#555" stroke-width="1.5"/></svg>
</div>

<div class="side-col"></div>

<div class="lbl" style="top:664px">JOBLEX Job Description:</div>
<p class="desc">Counsel individuals to maximize the independence and employability of persons coping with personal, social, and vocational difficulties that result from birth defects, illness, disease, accidents, aging, or the stress of daily life. Coordinate activities for residents of care and treatment facilities. Assess client needs and design and implement rehabilitation programs that may include personal and vocational counseling, training, and job placement.</p>
<div class="btn soft" style="top:901px;width:343px">LEARN MORE ABOUT THIS JOB ON JOBLEX</div>
<div class="btn deep" style="top:968px;width:210px">INDUSTRY INSIDER PAGE</div>

<div class="lbl" style="top:1051px">Top Tips:</div>
<p class="tip" style="top:1096px"><svg width="12" height="12" viewBox="0 0 12 12"><circle cx="6" cy="6" r="5" fill="none" stroke="var(--indigo)"/><path d="M3.5 6l1.8 1.8L8.7 4.3" fill="none" stroke="var(--indigo)"/></svg>Lorem Ipsum is simply dummy text of the printing and typesetting industry. Lorem Ipsum has been the industry's standard dummy text ever since</p>
<p class="tip" style="top:1188px"><svg width="12" height="12" viewBox="0 0 12 12"><circle cx="6" cy="6" r="5" fill="none" stroke="var(--indigo)"/><path d="M3.5 6l1.8 1.8L8.7 4.3" fill="none" stroke="var(--indigo)"/></svg>Lorem Ipsum is simply dummy text of the printing and typesetting industry. Lorem Ipsum has been the industry's standard dummy text ever since</p>

<div class="lbl" style="top:1289px">Preferred Online Programs:</div>
<div class="badge" style="left:366px;top:1343px;background:#6aa6c8"></div>
<div class="abs" style="left:600px;top:1343px;width:1px;height:134px;background:#ddd"></div>
<div class="badge" style="left:694px;top:1350px;width:106px;height:62px;background:#2e3b8c"></div>
<div class="prog-link" style="left:366px;top:1433px">Summit Mentor<br>Academy</div>
<div class="prog-link" style="left:694px;top:1433px">Global Guidance<br>Alliance</div>
<div class="btn soft" style="top:1515px;width:296px">VIEW LIFE COACHING PROGRAMS</div>

<svg class="abs" style="left:920px;top:665px" width="200" height="110" viewBox="0 0 200 110" aria-label="Match level gauge">
  <path d="M10 98A90 90 0 0 1 190 98" fill="none" stroke="#555" stroke-width="22"/>
  <path d="M10 98A90 90 0 0 1 190 98" fill="none" stroke="#fff" stroke-width="20"/>
  <path d="M22 98A78 78 0 0 1 45 43L73 71A38 38 0 0 0 62 98Z" fill="#d9282b"/>
  <path d="M45 43A78 78 0 0 1 78 23L88 61A38 38 0 0 0 73 71Z" fill="#ef7b22"/>
  <path d="M78 23A78 78 0 0 1 122 23L112 61A38 38 0 0 0 88 61Z" fill="#f2c71b"/>
  <path d="M122 23A78 78 0 0 1 155 43L127 71A38 38 0 0 0 112 61Z" fill="#9ac93c"/>
  <path d="M155 43A78 78 0 0 1 178 98L138 98A38 38 0 0 0 127 71Z" fill="#3aa645"/>
  <text x="14" y="78" font-size="8" font-family="Montserrat" font-weight="700" transform="rotate(-70 14 78)">LOW</text>
  <text x="32" y="38" font-size="8" font-family="Montserrat" font-weight="700" transform="rotate(-40 32 38)">FAIR</text>
  <text x="88" y="13" font-size="8" font-family="Montserrat" font-weight="700">GOOD</text>
  <text x="140" y="22" font-size="8" font-family="Montserrat" font-weight="700" transform="rotate(38 140 22)">GREAT</text>
  <text x="170" y="45" font-size="8" font-family="Montserrat" font-weight="700" transform="rotate(68 170 45)">EXCELLENT</text>
  <path d="M100 100L152 78" stroke="#333" stroke-width="5" stroke-linecap="round"/>
  <circle cx="100" cy="100" r="7" fill="#333"/>
</svg>
<div class="center-col" style="top:780px;font-size:16px;color:#333">Your match level (12)</div>
<div class="center-col" style="top:847px;font-family:'Quicksand',sans-serif;font-weight:700;font-size:22px">Average Salary:</div>
<div class="salary">$50,000</div>
<div class="center-col outlook" style="top:992px"><i></i>Rising Demand</div>
<div class="video" role="img" aria-label="Video about life coaching: a coach talking with clients"></div>
<svg class="abs" style="left:1000px;top:1185px" width="38" height="38" viewBox="0 0 38 38"><circle cx="19" cy="19" r="16" fill="none" stroke="#fff" stroke-width="2.5"/><path d="M15 11l11 8-11 8Z" fill="none" stroke="#fff" stroke-width="2.5" stroke-linejoin="round"/></svg>
<div class="center-col" style="top:1360px;font-size:16px;line-height:23px;color:#333">Minimum Qualifications<br>NONE</div>

<div class="jobs-by"><span>Jobs By</span><b><i></i>Hire Lantern</b></div>
<div class="field-lbl" style="left:343px">Job Title</div>
<div class="field-lbl" style="left:641px">Locations</div>
<div class="field" style="left:343px;top:1753px">Marketing</div>
<div class="field" style="left:639px;top:1753px">Longmont</div>
<div class="search">SEARCH</div>
<div class="abs" style="left:343px;top:1819px;width:780px;height:1px;background:#e2e2e2"></div>
<div class="field" style="left:343px;top:1838px">Within 50 Miles<svg width="13" height="8" viewBox="0 0 13 8"><path d="M1 1l5.5 5.5L12 1" fill="none" stroke="#888" stroke-width="1.3"/></svg></div>
<div class="field" style="left:639px;top:1838px">Posted anytime<svg width="13" height="8" viewBox="0 0 13 8"><path d="M1 1l5.5 5.5L12 1" fill="none" stroke="#888" stroke-width="1.3"/></svg></div>

<div class="result">Result <b>1 - 3</b> of <b>3900</b></div>
<div class="job-title">Digital Marketing Specialist</div>

<div class="meta" style="top:2025px"><svg width="16" height="14" viewBox="0 0 16 14"><rect x="1" y="3" width="14" height="10" fill="none" stroke="currentColor"/><path d="M5 3V1h6v2" fill="none" stroke="currentColor"/></svg>Lorem Ipsum is simply<span class="sp"></span><svg width="12" height="15" viewBox="0 0 12 15"><path d="M6 14S1 8.5 1 5.5a5 5 0 0 1 10 0C11 8.5 6 14 6 14Z" fill="none" stroke="currentColor"/><circle cx="6" cy="5.5" r="1.7" fill="none" stroke="currentColor"/></svg>dummy text of the printing</div>
<p class="job-desc" style="top:2058px">Lorem Ipsum is simply dummy text of the printing and typesetting industry. Lorem Ipsum has been the industry's standard dummy text ever since</p>

<div class="meta" style="top:2126px"><svg width="16" height="14" viewBox="0 0 16 14"><rect x="1" y="3" width="14" height="10" fill="none" stroke="currentColor"/><path d="M5 3V1h6v2" fill="none" stroke="currentColor"/></svg>Lorem Ipsum is simply<span class="sp"></span><svg width="12" height="15" viewBox="0 0 12 15"><path d="M6 14S1 8.5 1 5.5a5 5 0 0 1 10 0C11 8.5 6 14 6 14Z" fill="none" stroke="currentColor"/><circle cx="6" cy="5.5" r="1.7" fill="none" stroke="currentColor"/></svg>dummy text of the printing</div>
<p class="job-desc" style="top:2159px">Lorem Ipsum is simply dummy text of the printing and typesetting industry. Lorem Ipsum has been the industry's standard dummy text ever since</p>

<div class="meta" style="top:2227px"><svg width="16" height="14" viewBox="0 0 16 14"><rect x="1" y="3" width="14" height="10" fill="none" stroke="currentColor"/><path d="M5 3V1h6v2" fill="none" stroke="currentColor"/></svg>Lorem Ipsum is simply<span class="sp"></span><svg width="12" height="15" viewBox="0 0 12 15"><path d="M6 14S1 8.5 1 5.5a5 5 0 0 1 10 0C11 8.5 6 14 6 14Z" fill="none" stroke="currentColor"/><circle cx="6" cy="5.5" r="1.7" fill="none" stroke="currentColor"/></svg>dummy text of the printing</div>
<p class="job-desc" style="top:2260px">Lorem Ipsum is simply dummy text of the printing and typesetting industry. Lorem Ipsum has been the industry's standard dummy text ever since</p>

<footer class="footer"></footer>
<div class="social" style="left:433px"></div>
<div class="social" style="left:490px"></div>
<div class="social" style="left:547px"></div>
<div class="social alt" style="left:605px"></div>
<div class="social" style="left:662px"></div>
<div class="social" style="left:719px"><svg class="abs" style="left:15px;top:16px" width="18" height="16" viewBox="0 0 18 16"><path d="M1 6l8-5 8 5v9H1Z M1 6l8 5 8-5" fill="none" stroke="#fff" stroke-width="1.5" stroke-linejoin="round"/></svg></div>
<div class="foot-links"><span>News</span>I<span>Privacy Policy</span>I<span>Terms &amp; Conditions</span>I<span>Contact Us</span></div>
<div class="copy">Copyright © 2021 Copper Venture Company. All Right Reserved</div>

</body>
</html>
```